Smoker Oven Manufacturer Looking for Commercial Product Catalog

We are a small, family owned/operated international smoker oven manufacturer known for our end products and customer service. Our products include residential smokers, residential pellet grills, competition barbecue smokers, commercial smokers, commercial charbroilers, grilling and smoker accessories, sauces, spices, woods and food grade pellets. We have 6 international distributors and ship products everywhere.
Up until now, we have used individual spec sheets and a customized folder to send out information to prospects and we would like to move over to a catalog design.
We would like the final design to include red and our logo. The inside of the catalog is not as important to us as the cover, but we would like something that flows well. We like using food pictures as attention grabbers but also need balance so people who see our catalog do not think we are a restaurant. The end catalog will be about 20 pages.
Attached you will find examples of our spec sheets and the order we would like products in plus some of our current smoker images. For more information, please see our website: www.brinvale.com.
All of the product spec, past branding and content layout can be found in dropbox: https://www.filorama.net/sh/qp4tzwalbnro83x/KKTR2p9hqzvaTT5n1-dmWqx7b?dl=0

Target Market(s)

Owners/Operators/Chefs in the food industry

Industry/Entity Type

Commercial

Contact Information for Business Card

similar look and feel to the catalog

Colors
ec1f27
000000

Requirements
Must have
• Brinvale Logo, Red in the design but does not have to be the primary color used, products photos
Nice to have
• Food pictures

```html
<!DOCTYPE html>
<html lang="en">
<head>
<meta charset="utf-8">
<title>Brinvale Product Catalog 2017–2018 Cover</title>
<link href="https://fonts.googleapis.com/css2?family=Lato:wght@300;400;700;900&display=swap" rel="stylesheet">
<style>
  :root {
    --red: #ec1f27;
    --black: #000000;
    --ink: #111111;
    --navy: #1f3a8a;
    --paper: #e9e9eb;
    --white: #ffffff;
    --stage: #d9d4cc;
    --photo-dark: #3a1a0c;
    --photo-warm: #b8602a;
    --steel: #c9cdd2;
  }
  * { margin: 0; padding: 0; box-sizing: border-box; }
  html, body { width: 1200px; height: 804px; overflow: hidden; }
  body {
    background: var(--stage);
    font-family: "Lato", sans-serif;
    display: flex; align-items: center; justify-content: center;
  }
  .cover {
    position: relative;
    width: 520px; height: 728px;
    background: var(--paper);
    overflow: hidden;
    box-shadow: 0 10px 30px rgba(0,0,0,.25);
  }
  .cover-art { position: absolute; inset: 0; }
  .catalog-title {
    position: absolute; left: 70px; top: 360px;
    line-height: 1; font-weight: 300; letter-spacing: -0.5px;
  }
  .catalog-title .line-product { color: var(--white); font-size: 42px; display: block; }
  .catalog-title .line-catalog { color: var(--red); font-size: 42px; display: block; }
  .catalog-title .line-years {
    color: var(--white); font-size: 22px; letter-spacing: 9px; display: block; margin-top: 8px;
  }
  .site-url {
    position: absolute; left: 40px; top: 478px;
    color: var(--white); font-size: 11px; letter-spacing: 3px;
    transform: rotate(-5.2deg); transform-origin: left center;
  }
  .brand-name {
    position: absolute; left: 52px; top: 585px;
    color: var(--ink); font-weight: 900; font-size: 30px; letter-spacing: 1px;
    display: flex; align-items: center; gap: 10px;
  }
  .brand-name .brand-dot { width: 16px; height: 16px; background: var(--red); border-radius: 50%; }
  .about {
    position: absolute; left: 250px; top: 560px; width: 255px;
    transform: rotate(-5.2deg); transform-origin: left top;
  }
  .about .tagline { color: var(--navy); font-weight: 700; font-size: 12px; margin-bottom: 4px; }
  .about .blurb { color: var(--ink); font-size: 7.5px; line-height: 1.45; }
</style>
</head>
<body>
  <main class="cover">
    <svg class="cover-art" width="520" height="728" viewBox="0 0 520 728">
      <defs>
        <linearGradient id="roastTones" x1="0" y1="0" x2="1" y2="1">
          <stop offset="0" stop-color="#5a2410"/>
          <stop offset="0.5" stop-color="#b8602a"/>
          <stop offset="1" stop-color="#2a1208"/>
        </linearGradient>
        <linearGradient id="steelTones" x1="0" y1="0" x2="1" y2="1">
          <stop offset="0" stop-color="#e4e6e9"/>
          <stop offset="1" stop-color="#a9aeb4"/>
        </linearGradient>
      </defs>
      <rect class="black-field" x="0" y="0" width="520" height="520" fill="var(--black)"/>
      <rect class="hero-photo" x="0" y="0" width="520" height="300" fill="url(#roastTones)"
            role="img" aria-label="Photograph of golden roasted whole chickens on a smoker rack"/>
      <g class="accent-tiles" fill="#ffffff">
        <rect x="360" y="262" width="130" height="90" rx="8" opacity="0.25" transform="rotate(-14 425 307)"/>
        <rect x="300" y="330" width="70" height="48" rx="6" opacity="0.3" transform="rotate(-14 335 354)"/>
        <rect x="340" y="355" width="80" height="55" rx="6" opacity="0.3" transform="rotate(-14 380 382)"/>
        <rect x="400" y="335" width="70" height="55" rx="6" opacity="0.3" transform="rotate(-14 435 362)"/>
        <rect x="375" y="350" width="35" height="28" rx="4" opacity="0.35" transform="rotate(-14 392 364)"/>
      </g>
      <polygon class="gray-panel" points="0,512 520,465 520,728 0,728" fill="var(--paper)"/>
      <polygon class="red-band" points="0,494 520,447 520,465 0,512" fill="var(--red)"/>
      <g class="product-badges">
        <circle cx="345" cy="500" r="66" fill="var(--white)"/>
        <circle cx="345" cy="500" r="60" fill="url(#steelTones)"
                role="img" aria-label="Photograph of a stainless steel commercial smoker with closed doors"/>
        <circle cx="460" cy="462" r="66" fill="var(--white)"/>
        <circle cx="460" cy="462" r="60" fill="url(#steelTones)"
                role="img" aria-label="Photograph of an open commercial smoker oven showing rotating racks"/>
      </g>
    </svg>

    <h1 class="catalog-title">
      <span class="line-product">PRODUCT</span>
      <span class="line-catalog">CATALOG</span>
      <span class="line-years">2017-2018</span>
    </h1>

    <p class="site-url">www.brinvale.com</p>

    <div class="brand-name"><span class="brand-dot"></span>BRINVALE</div>

    <section class="about">
      <p class="tagline">We deliver the taste of barbecue to the world.</p>
      <p class="blurb">We have been manufacturing Smokers for over 50 years in Alder Falls, KS. Brinvale is the leading authority in barbecue cooking, products and technology. We provide high-end products with exceptional satisfaction to our customers.</p>
    </section>
  </main>
</body>
</html>
```